Need a business card for my new home staging and redesign business. Business name: Quillamore Interiors. Subtitle: Home styling and staging wizardry

Target Market(s)

Realtors, home sellers

Industry/Entity Type

Real Estate

Contact Information for Business Card

I don't have a website address yet, or a business Facebook account, but would like to include those. Do not have a logo or any graphics

Font styles to use
Sans Serif

Colors

Designer to choose colors to be used in the design.

Requirements
Must have
• Placeholders for contact details, e.g. Phone, email, web address, etc.
Nice to have
• Sophisticated but somewhat whimsical feel. Perhaps a stylized star (or magic wand?) over the "I" in interiors to convey inspiration.
Should not have
• Nothing too cutesy, including cartoon wizards.

```html
<!DOCTYPE html>
<html lang="en">
<head>
<meta charset="utf-8">
<title>Quillamore Interiors – Business Card</title>
<link rel="stylesheet" href="https://fonts.googleapis.com/css2?family=Josefin+Sans:wght@700&family=Open+Sans:wght@400;600&display=swap">
<style>
  :root {
    --page-bg: #e4e4e4;
    --card-bg: #363636;
    --card-ink: #ffffff;
    --card-shadow: rgba(0, 0, 0, 0.25);
  }
  * { margin: 0; padding: 0; box-sizing: border-box; }
  html, body {
    width: 1200px;
    height: 977px;
    overflow: hidden;
    background: var(--page-bg);
  }
  .canvas {
    width: 1200px;
    height: 977px;
    display: flex;
    flex-direction: column;
    align-items: center;
    justify-content: center;
    gap: 56px;
  }
  .card {
    position: relative;
    width: 700px;
    height: 400px;
    background: var(--card-bg);
    color: var(--card-ink);
    box-shadow: 0 8px 24px var(--card-shadow);
  }
  .brand {
    font-family: "Josefin Sans", sans-serif;
    font-weight: 700;
    text-transform: uppercase;
    letter-spacing: 0.06em;
    line-height: 1.02;
    color: var(--card-ink);
  }
  .card--front .brand {
    position: absolute;
    left: 130px;
    top: 138px;
    font-size: 60px;
  }
  .card--back .brand {
    position: absolute;
    left: 52px;
    bottom: 48px;
    font-size: 56px;
  }
  .contact {
    position: absolute;
    right: 48px;
    top: 44px;
    text-align: right;
    font-family: "Open Sans", sans-serif;
  }
  .contact__name {
    font-size: 22px;
    font-weight: 400;
    margin-right: 26px;
  }
  .contact__role {
    font-size: 12px;
    font-weight: 600;
    margin-right: 26px;
    margin-bottom: 20px;
  }
  .contact__list { list-style: none; }
  .contact__item {
    display: flex;
    align-items: center;
    justify-content: flex-end;
    gap: 12px;
    font-size: 13px;
    line-height: 24px;
  }
  .contact__icon {
    width: 14px;
    height: 14px;
    fill: var(--card-ink);
    flex: none;
  }
</style>
</head>
<body>
<main class="canvas">
  <section class="card card--front" aria-label="Card front">
    <h1 class="brand">Quillamore<br>Interiors</h1>
  </section>

  <section class="card card--back" aria-label="Card back">
    <div class="contact">
      <p class="contact__name">Elena Marsh</p>
      <p class="contact__role">General Manager</p>
      <ul class="contact__list">
        <li class="contact__item">(123) 456 7890
          <svg class="contact__icon" viewBox="0 0 16 16" aria-hidden="true"><path d="M3.6 1.2l2.2 2.6-1.3 1.7c.9 2 2.5 3.6 4.5 4.5l1.7-1.3 2.6 2.2-1.2 2.6C7.4 13.8 2.2 8.6 1 3.9z"/></svg>
        </li>
        <li class="contact__item">(123) 456 7890
          <svg class="contact__icon" viewBox="0 0 16 16" aria-hidden="true"><path d="M1 6c1.5-3 12.5-3 14 0l-.6 2-3-1V5.8C9.8 5.3 6.2 5.3 4.6 5.8V7l-3 1z"/><rect x="5" y="9" width="6" height="4" rx="1"/></svg>
        </li>
        <li class="contact__item">mail@quillamore.com
          <svg class="contact__icon" viewBox="0 0 16 16" aria-hidden="true"><path d="M1 3.5h14v9H1z M1.5 4l6.5 5 6.5-5" fill="none" stroke="#fff" stroke-width="1.4"/><path d="M1 3.5h14L8 9z"/></svg>
        </li>
        <li class="contact__item">www.quillamore.com
          <svg class="contact__icon" viewBox="0 0 16 16" aria-hidden="true"><circle cx="8" cy="8" r="7"/><path d="M1.5 8h13M8 1.2c-3 3.5-3 10 0 13.6M8 1.2c3 3.5 3 10 0 13.6" fill="none" stroke="#363636" stroke-width="1.1"/></svg>
        </li>
      </ul>
    </div>
    <h2 class="brand">Quillamore<br>Interiors</h2>
  </section>
</main>
</body>
</html>
```